Advertising flyer for proofreading business.

Hello everyone,

I need an advertising flyer for a new proofreading company in Australia.

I would like your design in be in two sizes:
- A4 (to be posted on noticeboards),
- A6 (to be printed in larger quantity to give away)
(please see the size specification file attached).

The text file is attached (Ad Text) and it contains lots of information. Please feel free to include your choice of text from the text file, but please include Poster title, and highlight 'ESL' and students discounts.

I understand that it is impossible to include the same amount of information on A6 and A4, so please feel free to chose what fits on each of them, but please keep the design similar.

I have attached our company logo, but feel free to adjust it to the poster design (feel free to change the color as well). The original logo file contains circle around it, please feel free to remove it and include only the typeset as it can be seen here: http://www.lexmarka.com.au/.

Flyers will be printed, so please see the specification file for details.

I will do my best to respond to feedback as soon as possible.

I appreciate your participation, time and help,
Best wishes,
Bartosz

Target Market(s)

Students, authors

Industry/Entity Type

Business

Colors

Designer to choose colors to be used in the design.

Requirements
Must have
• It would be good if poster is easy to spot on busy noticeboards and attract attention.
• Please keep the poster in the positive/optimistic mood, and so that it focuses on students, maybe photos of graduates(?).
• Poster title,
• Please include the list of proof-read documents as they are described in the attached text file (Ad Text).
• Please highlight students discounts and ESL.
Nice to have
• I would like to leave the creative freedom to all designers so at this point I have not adjusted the Look and Feel sliders. Please feel free to offer your own take on this.
• It would be nice if most of the text could be fit to the poster.

```html
<!DOCTYPE html>
<html lang="en">
<head>
<meta charset="utf-8">
<title>Lexmarka – Proofreading Flyer A4 and A6</title>
<link href="https://fonts.googleapis.com/css2?family=Barlow+Semi+Condensed:wght@300;400;600;700&display=swap" rel="stylesheet">
<style>
  :root{
    --stage:#1c1c1c;
    --charcoal:#2e3134;
    --teal:#23b596;
    --teal-deep:#137a66;
    --mist:#ececec;
    --mist-dark:#cfcfcf;
    --lime:#86b53c;
    --ink:#1e1e1e;
    --white:#ffffff;
  }
  *{margin:0;padding:0;box-sizing:border-box}
  html,body{width:1200px;height:1000px;overflow:hidden;background:var(--stage)}
  body{position:relative;font-family:"Barlow Semi Condensed",sans-serif}

  .flyer{position:absolute;width:585px;height:821px;overflow:hidden;
    background:radial-gradient(ellipse at 40% 60%,#f7f7f7 0%,var(--mist) 55%,var(--mist-dark) 100%);
    transform-origin:0 0}
  .flyer--a4{left:146px;top:85px}
  .flyer--a6{left:762px;top:286px;transform:scale(0.511)}

  .header-band{position:absolute;left:0;top:0;width:585px;height:300px}
  .footer-band{position:absolute;left:0;bottom:0;width:585px;height:90px}

  .brand{position:absolute;left:38px;top:46px;display:flex;align-items:center;gap:6px;
    color:var(--white);font-weight:300;font-size:34px;line-height:1;white-space:nowrap}
  .brand__dot{width:10px;height:10px;border-radius:50%;background:var(--teal)}
  .title{position:absolute;left:205px;top:30px;color:var(--teal);font-weight:400;
    font-size:31px;line-height:37px;letter-spacing:.3px;white-space:nowrap}

  .intro{position:absolute;left:0;width:585px;text-align:center;color:var(--white)}
  .intro--lead{top:114px;font-size:21px;font-weight:300}
  .intro--esl{top:155px;font-size:15px;line-height:19px;font-weight:300}
  .intro--esl strong{font-weight:600}
  .intro--style{top:220px;font-size:15px;font-weight:300}
  .intro--speed{top:246px;font-size:15px;font-weight:300}

  .magnifier{position:absolute;left:362px;top:293px;width:223px;height:172px;
    background:radial-gradient(circle at 58% 48%,#fafafa 0%,#dcdcdc 50%,#a5a5a5 72%,#e6e6e6 90%,transparent 100%);
    border-radius:4px}

  .section-heading{position:absolute;color:var(--teal-deep);font-weight:700;font-size:16.5px;letter-spacing:.2px}
  .doc-types__heading{left:29px;top:314px}
  .doc-types{position:absolute;left:29px;top:336px;list-style:none;color:var(--ink);
    font-size:16.5px;line-height:19.8px;font-weight:400}

  .price__heading{left:46px;top:455px}
  .price{position:absolute;left:46px;top:480px;width:530px;list-style:none;color:var(--ink);
    font-size:15.5px;line-height:19.6px}
  .price li{position:relative;margin-bottom:4px}
  .price li::before{content:"";position:absolute;left:-16px;top:7px;width:6px;height:6px;
    border-radius:50%;background:var(--ink)}

  .testimonial__heading{left:27px;top:674px;font-size:14.5px}
  .testimonial{position:absolute;left:27px;top:692px;width:540px;color:var(--ink);
    font-size:14.5px;line-height:18.5px}

  .contact{position:absolute;left:29px;top:772px;color:var(--white);font-size:15px;line-height:19px;font-weight:300}
  .contact strong{font-weight:600}
  .signature{position:absolute;left:403px;top:755px;color:var(--white);font-size:15px;line-height:18.5px;font-weight:300}
  .signature strong{font-weight:600}
</style>
</head>
<body>

<article class="flyer flyer--a4">
  <svg class="header-band" viewBox="0 0 585 300" preserveAspectRatio="none" aria-hidden="true">
    <path d="M0 0H585V285C470 270 380 272 290 282C180 294 80 292 0 288Z" fill="#5a5d60"/>
    <path d="M0 0H585V277C470 264 380 266 290 276C180 288 80 286 0 282Z" fill="var(--charcoal)"/>
  </svg>
  <svg class="footer-band" viewBox="0 0 585 90" preserveAspectRatio="none" aria-hidden="true">
    <path d="M0 16C140 0 300 -2 440 4C510 7 560 14 585 20V90H0Z" fill="var(--lime)"/>
  </svg>

  <div class="brand"><span class="brand__dot"></span>Lexmarka</div>
  <h1 class="title">PROFESSIONAL<br>PROOFREADING SERVICES.</h1>

  <p class="intro intro--lead">Professional , English-language proofreading:</p>
  <p class="intro intro--esl">Help with English as a second language<br><strong>(ESL - native English speaker with English Honours degree<br>will correct all English language errors, spelling and grammar mistakes.</strong></p>
  <p class="intro intro--style">Includes referencing and editing for style, coherence and clarity</p>
  <p class="intro intro--speed">Fast, negotiable time-frames.</p>

  <div class="magnifier" role="img" aria-label="Illustration of a magnifying glass over a page of text"></div>

  <h2 class="section-heading doc-types__heading">TYPES OF PROOF-READ DOCUMENTS:</h2>
  <ul class="doc-types">
    <li>Essays / Assignments / Theses / Resumes</li>
    <li>Business Correspondence / Training manuals</li>
    <li>Newsletters Advertising copy / Brochures</li>
    <li>Catalogues / Media releases / Websites</li>
    <li>Presentations / Speeches / Novels / Short stories</li>
  </ul>

  <h2 class="section-heading price__heading">PRICE GUIDE:</h2>
  <ul class="price">
    <li>Prices starting at $20 per page. Additional charges may apply for longer and/<br>or more complex documents (e.g. documents requiring<br>specialist help with English as a second language).</li>
    <li>Discounts for not-for-profit organisations and students.<br>Special student discount rate: $25 per hour -<br>roughly 1000 words (4 pages) of well-written text.</li>
    <li>Package deals on documents over 50,000 words.</li>
    <li>Fast turnaround times (same day service can be provided by special arrangement).</li>
  </ul>

  <h2 class="section-heading testimonial__heading">TESTIMONIAL:</h2>
  <p class="testimonial">“Hannah understood our requirements quickly and has been fantastic at delivering quality work, on time and within agreed budget. It's a pleasure to work with her.”</p>

  <p class="contact">Contact us for an obligation-free quote:<br><strong>0400 555 182 / proofing@lexmarka.com.au</strong></p>
  <p class="signature"><strong>Carol Dawson</strong><br>Operations Manager<br>Meridian Group</p>
</article>

<article class="flyer flyer--a6">
  <svg class="header-band" viewBox="0 0 585 300" preserveAspectRatio="none" aria-hidden="true">
    <path d="M0 0H585V285C470 270 380 272 290 282C180 294 80 292 0 288Z" fill="#5a5d60"/>
    <path d="M0 0H585V277C470 264 380 266 290 276C180 288 80 286 0 282Z" fill="var(--charcoal)"/>
  </svg>
  <svg class="footer-band" viewBox="0 0 585 90" preserveAspectRatio="none" aria-hidden="true">
    <path d="M0 16C140 0 300 -2 440 4C510 7 560 14 585 20V90H0Z" fill="var(--lime)"/>
  </svg>

  <div class="brand"><span class="brand__dot"></span>Lexmarka</div>
  <h1 class="title">PROFESSIONAL<br>PROOFREADING SERVICES.</h1>

  <p class="intro intro--lead">Professional , English-language proofreading:</p>
  <p class="intro intro--esl">Help with English as a second language<br><strong>(ESL - native English speaker with English Honours degree<br>will correct all English language errors, spelling and grammar mistakes.</strong></p>
  <p class="intro intro--style">Includes referencing and editing for style, coherence and clarity</p>
  <p class="intro intro--speed">Fast, negotiable time-frames.</p>

  <div class="magnifier" role="img" aria-label="Illustration of a magnifying glass over a page of text"></div>

  <h2 class="section-heading doc-types__heading">TYPES OF PROOF-READ DOCUMENTS:</h2>
  <ul class="doc-types">
    <li>Essays / Assignments / Theses / Resumes</li>
    <li>Business Correspondence / Training manuals</li>
    <li>Newsletters Advertising copy / Brochures</li>
    <li>Catalogues / Media releases / Websites</li>
    <li>Presentations / Speeches / Novels / Short stories</li>
  </ul>

  <h2 class="section-heading price__heading">PRICE GUIDE:</h2>
  <ul class="price">
    <li>Prices starting at $20 per page. Additional charges may apply for longer and/<br>or more complex documents (e.g. documents requiring<br>specialist help with English as a second language).</li>
    <li>Discounts for not-for-profit organisations and students.<br>Special student discount rate: $25 per hour -<br>roughly 1000 words (4 pages) of well-written text.</li>
    <li>Package deals on documents over 50,000 words.</li>
    <li>Fast turnaround times (same day service can be provided by special arrangement).</li>
  </ul>

  <h2 class="section-heading testimonial__heading">TESTIMONIAL:</h2>
  <p class="testimonial">“Hannah understood our requirements quickly and has been fantastic at delivering quality work, on time and within agreed budget. It's a pleasure to work with her.”</p>

  <p class="contact">Contact us for an obligation-free quote:<br><strong>0400 555 182 / proofing@lexmarka.com.au</strong></p>
  <p class="signature"><strong>Carol Dawson</strong><br>Operations Manager<br>Meridian Group</p>
</article>

</body>
</html>
```